Business car for dental practice

I have a new logo. Want it use for a new business card design. Hi end dental practice Would like a scan code on it for quick access to my web site and mobile site too. Green and purple are in logo design. Maybe have scan code on back? My website is peterhalvorsenDDS.example
Updates

Lakemont Crest Dental Associates

248 N Fairlawn Ave
Harrow Glen, NY 10990
555-318-4072

317 N Wexford Rd. 
Suite 406
Brookmere, NY 10971
555-762-1938

would like to incorporate logo, and addresses of both offices, and I recently saw a business card with a scan box on it which would bring people directly to the web site. if anyone knows how to do that, that could possibly go on the back of the card. (May be something I have to add at printing process) card can be one sided, or two sided.  

Reason: designer is revising for me. has not posted changes yet. hope he does soon!!

Industry/Entity Type

Business

```html
<!DOCTYPE html>
<html lang="en">
<head>
<meta charset="utf-8">
<title>Lakemont Crest Dental Associates – Business Card</title>
<link rel="stylesheet" href="https://fonts.googleapis.com/css2?family=PT+Sans:ital,wght@0,400;0,700;1,400&display=swap">
<style>
  :root {
    --backdrop: #2b2b2b;
    --plum: #6a1a5c;
    --plum-deep: #561449;
    --plum-panel: #4a1140;
    --leaf: #3f9a3a;
    --paper: #ffffff;
    --paper-shade: #e9e9e9;
    --ink-light: #ffffff;
    --ink-band: #dff0dc;
  }
  * { box-sizing: border-box; margin: 0; padding: 0; }
  html, body {
    width: 1200px; height: 900px; overflow: hidden;
    background: var(--backdrop);
    font-family: "PT Sans", sans-serif;
  }
  .stage {
    width: 1200px; height: 900px;
    display: flex; flex-direction: column;
    align-items: center; justify-content: center; gap: 50px;
  }
  .card {
    position: relative;
    width: 665px; height: 380px;
    overflow: hidden;
    box-shadow: 0 10px 30px rgba(0,0,0,.45);
  }

  /* Back side */
  .card-back { background: var(--plum); }
  .back-panel {
    position: absolute; top: 0; right: 0;
    width: 300px; height: 210px;
    background: var(--plum-deep);
  }
  .back-panel-square {
    position: absolute; top: 30px; right: 90px;
    width: 150px; height: 150px;
    background: var(--plum-panel);
    border-radius: 6px;
  }
  .name-band {
    position: absolute; left: 0; top: 160px;
    width: 290px; height: 64px;
    background: var(--leaf);
    padding: 9px 0 0 58px;
    color: var(--ink-light);
  }
  .name-band .person { font-weight: 700; font-size: 20px; line-height: 1.1; }
  .name-band .role { font-style: italic; font-size: 17px; color: var(--ink-band); }
  .offices {
    position: absolute; left: 330px; top: 150px;
    color: var(--ink-light);
    font-size: 17px; line-height: 1.25;
  }
  .office { font-style: normal; }
  .office + .office { margin-top: 16px; }

  /* Front side */
  .card-front {
    background: linear-gradient(160deg, var(--paper) 40%, var(--paper-shade) 100%);
    display: flex; align-items: center; justify-content: center; gap: 22px;
  }
  .brand-square {
    width: 118px; height: 118px;
    background: var(--plum);
    flex: none;
  }
  .brand-name {
    color: var(--plum);
    font-weight: 400;
    line-height: 1;
  }
  .brand-name .line-main { display: block; font-size: 52px; }
  .brand-name .line-sub { display: block; font-size: 26px; letter-spacing: 6px; margin-top: 8px; }
</style>
</head>
<body>
<main class="stage">
  <section class="card card-back" aria-label="Card back">
    <div class="back-panel"><div class="back-panel-square"></div></div>
    <div class="name-band">
      <p class="person">John Doe</p>
      <p class="role">Designation</p>
    </div>
    <div class="offices">
      <address class="office">248 N Fairlawn Ave<br>Harrow Glen, NY 10990<br>Tel: 555-318-4072</address>
      <address class="office">317 N Wexford Rd. Suite 406<br>Brookmere, NY 10971<br>Tel: 555-762-1938</address>
    </div>
  </section>

  <section class="card card-front" aria-label="Card front">
    <div class="brand-square"></div>
    <h1 class="brand-name">
      <span class="line-main">Lakemont Crest</span>
      <span class="line-sub">Dental Associates</span>
    </h1>
  </section>
</main>
</body>
</html>
```